Tavisco hd highway sign

would like a comercial truck in backround, and would like it very easy to read. Must have company name Tavisco H.D. Mechanical
would like address included 5912 quillby frontage road. would a some bullet points on sign
-Commercial truck and trailer inspection and repair
-Heavy equipment repair
-24/7 Mobile service

```html
<!DOCTYPE html>
<html lang="en">
<head>
<meta charset="utf-8">
<title>Tavisco H.D. Mechanical – Highway Sign</title>
<link rel="stylesheet" href="https://fonts.googleapis.com/css2?family=Saira+Semi+Condensed:wght@500;600;700&display=swap">
<style>
  :root {
    --teal: #55c2c3;
    --night: #1b1a24;
    --violet-dark: #1f1a33;
    --violet: #3a3157;
    --violet-light: #4a4070;
    --white: #ffffff;
    --ink: #1d1c28;
    --backdrop: #e8ecef;
  }
  * { margin: 0; padding: 0; box-sizing: border-box; }
  html, body { width: 1200px; height: 720px; overflow: hidden; background: var(--backdrop); }
  body { font-family: "Saira Semi Condensed", "Arial Narrow", sans-serif; }

  .sign {
    position: absolute; left: 40px; top: 100px;
    width: 1120px; height: 520px;
    overflow: hidden;
    box-shadow: 0 14px 40px rgba(20, 20, 40, 0.25);
  }
  .truck-photo {
    position: absolute; left: 0; top: 14px; width: 1120px; height: 330px;
    background:
      radial-gradient(ellipse 340px 200px at 430px 200px, rgba(85, 194, 195, 0.28), transparent 70%),
      radial-gradient(ellipse 500px 300px at 900px 140px, var(--violet-light), transparent 75%),
      linear-gradient(100deg, var(--violet-dark) 0%, var(--violet) 60%, var(--violet-light) 100%);
  }
  .sign-shapes { position: absolute; inset: 0; }

  .company-name {
    position: absolute; left: 680px; top: 88px;
    color: var(--white);
    font-weight: 600; font-size: 50px; line-height: 1;
    letter-spacing: 1px; text-transform: uppercase;
    white-space: nowrap;
  }

  .service {
    position: absolute; width: 250px; margin-left: -125px;
    text-align: center; color: var(--ink);
    font-weight: 700; font-size: 20px; line-height: 1.1;
    text-transform: uppercase; white-space: nowrap;
  }
  .service--inspection { left: 250px; top: 372px; }
  .service--equipment  { left: 500px; top: 366px; }
  .service--mobile     { left: 780px; top: 360px; }

  .address {
    position: absolute; left: 0; right: 0; top: 450px; height: 70px;
    display: flex; justify-content: center; align-items: center; gap: 12px;
    color: var(--white);
    font-weight: 600; font-size: 26px; letter-spacing: 0.5px;
    text-transform: uppercase; white-space: nowrap;
  }
  .address svg { width: 18px; height: 26px; }
</style>
</head>
<body>
<main class="sign">
  <div class="truck-photo" role="img" aria-label="Commercial semi truck outlined in glowing teal light, driving at night"></div>

  <svg class="sign-shapes" viewBox="0 0 1120 520" width="1120" height="520" aria-hidden="true">
    <!-- top band -->
    <rect x="0" y="0" width="850" height="14" fill="var(--teal)"/>
    <rect x="850" y="0" width="270" height="14" fill="var(--night)"/>

    <!-- service panel -->
    <polygon points="0,328 1120,298 1120,316 0,346" fill="var(--teal)"/>
    <polygon points="0,346 1120,316 1120,450 0,450" fill="var(--white)"/>

    <!-- dividers -->
    <line x1="378" y1="372" x2="378" y2="440" stroke="var(--teal)" stroke-width="2" stroke-dasharray="5 4"/>
    <line x1="648" y1="362" x2="648" y2="432" stroke="var(--teal)" stroke-width="2" stroke-dasharray="5 4"/>

    <!-- address bar -->
    <polygon points="935,426 1120,420 1120,450 950,450" fill="var(--teal)"/>
    <polygon points="0,450 120,450 95,520 0,520" fill="var(--teal)"/>
    <polygon points="120,450 1120,450 1120,520 95,520" fill="var(--night)"/>

    <!-- icon: truck -->
    <g class="icon icon--truck" transform="translate(250 330)">
      <circle r="38" fill="var(--white)"/>
      <circle r="32" fill="none" stroke="var(--teal)" stroke-width="5"/>
      <g fill="none" stroke="var(--ink)" stroke-width="1.6" stroke-linejoin="round">
        <path d="M-2 -16 h12 l3 8 v18 h-15 z"/>
        <rect x="1" y="-12" width="8" height="6"/>
        <path d="M-20 6 h18 v4 h-18 z"/>
        <circle cx="-14" cy="13" r="3.5"/>
        <circle cx="5" cy="13" r="3.5"/>
        <circle cx="12" cy="13" r="3.5"/>
      </g>
    </g>

    <!-- icon: gear and wrench -->
    <g class="icon icon--gear" transform="translate(500 323)">
      <circle r="38" fill="var(--white)"/>
      <circle r="32" fill="none" stroke="var(--teal)" stroke-width="5"/>
      <g fill="none" stroke="var(--ink)" stroke-width="1.6">
        <circle r="13" stroke-dasharray="5 3" stroke-width="5"/>
        <circle r="7"/>
        <path d="M-4 -4 L14 14" stroke-width="3" stroke-linecap="round"/>
      </g>
    </g>

    <!-- icon: 24 hour clock -->
    <g class="icon icon--clock" transform="translate(780 316)">
      <circle r="38" fill="var(--white)"/>
      <circle r="32" fill="none" stroke="var(--teal)" stroke-width="5"/>
      <g fill="none" stroke="var(--ink)" stroke-width="1.6" stroke-linecap="round">
        <path d="M-16 6 A17 17 0 1 1 6 16"/>
        <path d="M-19 1 l3 5 l5 -3"/>
      </g>
      <text x="1" y="4" text-anchor="middle" font-family="Saira Semi Condensed, sans-serif" font-weight="600" font-size="13" fill="var(--ink)">24</text>
    </g>
  </svg>

  <h1 class="company-name">Tavisco H.D.<br>Mechanical</h1>

  <p class="service service--inspection">Commercial truck<br>and trailer<br>inspection and repair</p>
  <p class="service service--equipment">Heavy<br>equipment<br>repair</p>
  <p class="service service--mobile">24/7<br>mobile<br>service</p>

  <p class="address">
    <svg viewBox="0 0 18 26" aria-hidden="true">
      <path d="M9 0 C4 0 0 4 0 9 C0 15 9 26 9 26 C9 26 18 15 18 9 C18 4 14 0 9 0 Z" fill="var(--teal)"/>
      <circle cx="9" cy="9" r="3.5" fill="var(--night)"/>
    </svg>
    5912 Quillby Frontage Road
  </p>
</main>
</body>
</html>
```